Business Card Design

I need a business card design for a new business based in South West Australia.
I specialize in residential window cleaning & general handyman maintenance.

Industry/Entity Type

Business

Contact Information for Business Card

Dale Marsh - 512 SILVER HAWK DETAILING
- Window Cleaning
- House Maintenance

```html
<!DOCTYPE html>
<html lang="en">
<head>
<meta charset="utf-8">
<title>512 Silver Hawk Detailing – Business Card</title>
<link rel="stylesheet" href="https://fonts.googleapis.com/css2?family=Arimo:wght@400;700&family=Old+Standard+TT:wght@700&display=swap">
<style>
  :root {
    --page-bg: #e9e6e1;
    --glass-light: #dbe9f6;
    --glass-mid: #b9d2ea;
    --glass-deep: #9fbfdf;
    --stripe-blue: #1f74c8;
    --card-black: #0b0b0c;
    --card-black-soft: #1e1f22;
    --ink: #0a0a0a;
    --name-grey: #e6e6e6;
    --service-white: #ffffff;
  }
  * { margin: 0; padding: 0; box-sizing: border-box; }
  html, body { width: 1200px; height: 892px; overflow: hidden; background: var(--page-bg); }
  .card {
    position: absolute; left: 110px; top: 166px;
    width: 980px; height: 560px;
    border-radius: 6px; overflow: hidden;
    box-shadow: 0 14px 40px rgba(0,0,0,0.25);
  }
  .card-art { position: absolute; inset: 0; }
  .company-name {
    position: absolute; left: 228px; top: 120px;
    font-family: "Arimo", sans-serif; font-weight: 700;
    font-size: 46px; letter-spacing: 0.5px; color: var(--ink);
    white-space: nowrap;
  }
  .tagline {
    position: absolute; left: 138px; top: 176px;
    font-family: "Old Standard TT", serif; font-weight: 700;
    font-size: 23px; color: var(--ink); white-space: nowrap;
  }
  .person-name {
    position: absolute; left: 72px; top: 372px;
    font-family: "Old Standard TT", serif; font-weight: 700;
    font-size: 50px; color: var(--name-grey); white-space: nowrap;
  }
  .services {
    position: absolute; left: 500px; top: 352px;
    list-style: none;
  }
  .service {
    display: flex; align-items: center; gap: 30px;
    height: 58px;
    font-family: "Arimo", sans-serif; font-size: 36px;
    color: var(--service-white); white-space: nowrap;
  }
  .service svg { width: 26px; height: 26px; flex: none; }
</style>
</head>
<body>
  <div class="card">
    <svg class="card-art" viewBox="0 0 980 560" width="980" height="560">
      <defs>
        <linearGradient id="glass" x1="0" y1="0" x2="1" y2="1">
          <stop offset="0" stop-color="var(--glass-mid)"/>
          <stop offset="0.5" stop-color="var(--glass-light)"/>
          <stop offset="1" stop-color="var(--glass-deep)"/>
        </linearGradient>
        <linearGradient id="gloss" x1="0" y1="0" x2="0.4" y2="1">
          <stop offset="0" stop-color="var(--card-black-soft)"/>
          <stop offset="0.6" stop-color="var(--card-black)"/>
          <stop offset="1" stop-color="var(--card-black)"/>
        </linearGradient>
      </defs>
      <rect class="glass-photo" role="img" aria-label="Photo of a worker on a lift platform cleaning a glass building facade" x="0" y="0" width="980" height="300" fill="url(#glass)"/>
      <polygon class="accent-stripe" points="0,182 102,232 980,256 980,270 98,246 0,196" fill="var(--stripe-blue)"/>
      <polygon class="dark-panel" points="0,206 96,256 980,282 980,560 0,560" fill="url(#gloss)"/>
    </svg>

    <div class="company-name">512 SILVER HAWK DETAILING</div>
    <div class="tagline">residential window cleaning &amp; general handyman maintenance</div>

    <div class="person-name">Dale Marsh</div>

    <ul class="services">
      <li class="service">
        <svg viewBox="0 0 26 26" aria-hidden="true"><circle cx="13" cy="13" r="9" fill="none" stroke="#fff" stroke-width="2"/><circle cx="13" cy="13" r="3.5" fill="#fff"/><path d="M13 0v6M13 20v6M0 13h6M20 13h6" stroke="#fff" stroke-width="2"/></svg>
        Window Cleaning
      </li>
      <li class="service">
        <svg viewBox="0 0 26 26" aria-hidden="true"><circle cx="13" cy="13" r="9" fill="none" stroke="#fff" stroke-width="2"/><circle cx="13" cy="13" r="3.5" fill="#fff"/><path d="M13 0v6M13 20v6M0 13h6M20 13h6" stroke="#fff" stroke-width="2"/></svg>
        House Maintenance
      </li>
    </ul>
  </div>
</body>
</html>
```